Platelet Rich Plasma (PRP) Flyer

Hi,

Looking to spruce up our Platelet Rich Plasma Flyer (see power point attachment). I also included previous flyers as examples on the design style we are looking for.

Quorum is our official font of our logo.
Attached is our logo in EPS format.
Please use the current photos in the power point. If you include photos, please make sure the stock image is free.

Files must be under 5MB. JPEG, PNG, PDF, .ai

Thank you,
Dorian

Target Market(s)

Patients

Industry/Entity Type

Healthcare

Font styles to use
Other font styles liked:
• Quorum

Requirements
Must have
• Emphasis on Platelet Rich Plasma Therapy when they pick up the flyer. The price of $199. FSA/HSA Eligible. The different treatment areas. The three addresses. Best of the best logo can be very small, not as important.
Nice to have
• One or two pictures. Less is more
Should not have
• Long paragraphs, multiple sentences.

```html
<!DOCTYPE html>
<html lang="en">
<head>
<meta charset="utf-8">
<title>Platelet Rich Plasma Therapy Flyer</title>
<link rel="stylesheet" href="https://fonts.googleapis.com/css2?family=Oxanium:wght@500;700&family=Russo+One&family=Roboto+Condensed:wght@400;700&display=swap">
<style>
  :root {
    --paper: #e9e9e7;
    --charcoal: #333333;
    --teal: #2fd1a8;
    --orange: #fb7f3c;
    --white: #ffffff;
    --ink: #111111;
    --torn-grey: #b5b5b5;
  }
  * { margin: 0; padding: 0; box-sizing: border-box; }
  html, body { width: 1082px; height: 1200px; overflow: hidden; background: var(--paper); }
  .flyer { position: relative; width: 1082px; height: 1200px; background: var(--paper); overflow: hidden; }
  .shape-layer { position: absolute; left: 0; top: 0; }

  .brand { position: absolute; left: 150px; top: 20px; font-family: "Oxanium", sans-serif; font-weight: 700; color: var(--orange); font-size: 32px; line-height: 1.02; text-transform: uppercase; }
  .brand-mark { position: absolute; left: -48px; top: 22px; width: 30px; height: 30px; background: var(--orange); }

  .services { position: absolute; left: 585px; top: 22px; font-family: "Russo One", sans-serif; color: var(--ink); font-size: 29px; line-height: 37px; text-transform: uppercase; white-space: nowrap; }
  .phone { position: absolute; left: 655px; top: 146px; font-family: "Russo One", sans-serif; font-size: 36px; line-height: 44px; color: var(--ink); display: flex; align-items: center; gap: 14px; white-space: nowrap; }

  .title { position: absolute; left: 40px; top: 230px; width: 1002px; text-align: center; font-family: "Russo One", sans-serif; color: var(--orange); font-size: 46px; line-height: 56px; font-weight: 400; text-transform: uppercase; white-space: nowrap; }

  .info-box { position: absolute; left: 46px; top: 355px; width: 465px; height: 427px; background: var(--charcoal); color: var(--white); font-family: "Roboto Condensed", sans-serif; text-transform: uppercase; padding: 40px 28px 0 28px; }
  .info-line { font-size: 24px; line-height: 1.3; }
  .info-line + .info-line { margin-top: 14px; }
  .price { margin-top: 34px; font-family: "Russo One", sans-serif; color: var(--orange); font-size: 72px; line-height: 1; }
  .price-note { margin-top: 12px; font-family: "Russo One", sans-serif; color: var(--teal); font-size: 28px; line-height: 1.1; }

  .treating { position: absolute; left: 46px; top: 822px; width: 560px; font-family: "Oxanium", sans-serif; font-weight: 500; color: var(--charcoal); font-size: 32px; line-height: 40px; text-transform: uppercase; }

  .offices { position: absolute; left: 0; top: 1066px; width: 1082px; font-family: "Roboto Condensed", sans-serif; color: var(--white); text-align: center; }
  .office { position: absolute; top: 0; width: 340px; }
  .office:nth-child(1) { left: 32px; }
  .office:nth-child(2) { left: 395px; }
  .office:nth-child(3) { left: 741px; }
  .office-name { font-family: "Oxanium", sans-serif; font-weight: 700; font-size: 26px; line-height: 32px; text-decoration: underline; text-transform: uppercase; margin-bottom: 8px; }
  .office-address { font-size: 17px; line-height: 22px; text-transform: uppercase; }
</style>
</head>
<body>
<main class="flyer">
  <svg class="shape-layer" width="1082" height="1200" viewBox="0 0 1082 1200">
    <defs>
      <linearGradient id="lab-tone" x1="0" y1="0" x2="1" y2="1">
        <stop offset="0" stop-color="#f2f2f2"/><stop offset="0.55" stop-color="#9aa1a8"/><stop offset="1" stop-color="#3d4650"/>
      </linearGradient>
      <linearGradient id="foot-tone" x1="0" y1="0" x2="1" y2="1">
        <stop offset="0" stop-color="#2c4a5c"/><stop offset="0.5" stop-color="#8a5a45"/><stop offset="1" stop-color="#223c4c"/>
      </linearGradient>
    </defs>

    <!-- header bands -->
    <path class="header-swoop" d="M0 114 H480 C530 114 555 130 585 165 C610 195 630 209 680 209 H1082 V230 H0 Z" fill="var(--charcoal)"/>
    <path class="header-teal" d="M0 145 H500 C530 145 545 160 562 180 L586 209 H0 Z" fill="var(--teal)"/>
    <path class="title-underline" d="M0 298 C320 330 720 335 1082 282 V300 C720 355 320 352 0 322 Z" fill="var(--teal)"/>
    <path class="title-bar" d="M0 209 H1082 V282 C720 330 320 326 0 298 Z" fill="var(--charcoal)"/>

    <!-- accent diamonds -->
    <rect x="-55" y="-55" width="110" height="110" fill="var(--teal)" transform="translate(1030 424) rotate(45)"/>
    <rect x="-55" y="-55" width="110" height="110" fill="var(--orange)" transform="translate(1073 595) rotate(45)"/>
    <rect x="-55" y="-55" width="110" height="110" fill="var(--orange)" transform="translate(606 706) rotate(45)"/>
    <rect x="-65" y="-65" width="130" height="130" fill="var(--teal)" transform="translate(1090 892) rotate(45)"/>

    <!-- photo diamonds -->
    <g transform="translate(718 526) rotate(45)">
      <rect x="-116" y="-116" width="232" height="232" fill="var(--teal)"/>
      <rect x="-107" y="-107" width="214" height="214" fill="url(#lab-tone)" role="img" aria-label="Photo: gloved hands placing blood sample tubes into a centrifuge"/>
    </g>
    <g transform="translate(870 773) rotate(45)">
      <rect x="-120" y="-120" width="240" height="240" fill="var(--teal)"/>
      <rect x="-111" y="-111" width="222" height="222" fill="url(#foot-tone)" role="img" aria-label="Photo: person holding a painful ankle and heel"/>
    </g>

    <!-- torn edge and footer -->
    <path class="torn-grey" d="M0 970 L30 964 L55 972 L90 962 L120 970 L160 960 L200 971 L240 963 L275 969 L310 958 L350 970 L395 962 L430 971 L470 959 L510 968 L550 961 L590 972 L630 960 L670 969 L710 962 L750 970 L790 959 L830 968 L870 961 L910 971 L950 960 L990 969 L1030 962 L1082 968 V1000 H0 Z" fill="var(--torn-grey)"/>
    <path class="torn-white" d="M0 982 L40 978 L80 986 L120 977 L165 984 L210 976 L250 985 L300 978 L345 987 L390 977 L440 984 L490 978 L540 988 L590 977 L640 985 L690 979 L740 987 L790 978 L840 984 L890 976 L940 986 L990 978 L1040 984 L1082 979 V1012 H0 Z" fill="var(--white)"/>
    <path class="footer" d="M0 1004 L45 996 L95 1008 L140 998 L190 1010 L240 997 L290 1007 L340 999 L390 1011 L440 998 L490 1008 L540 997 L590 1007 L640 999 L690 1010 L740 998 L790 1008 L840 999 L890 1010 L940 997 L990 1007 L1040 998 L1082 1004 V1200 H0 Z" fill="var(--charcoal)"/>
  </svg>

  <div class="brand"><span class="brand-mark"></span>Ridgeview<br>Foot &amp; Ankle<br>Millbrook</div>

  <div class="services">Podiatry | Foot &amp; Ankle<br>Surgery Sports Medicine<br>| Wound Care</div>

  <div class="phone">
    <svg width="36" height="36" viewBox="0 0 36 36" aria-hidden="true">
      <circle cx="18" cy="18" r="18" fill="var(--ink)"/>
      <path d="M11 9 L15 9 L17 14 L14.5 16 C15.8 19 17.5 20.8 20.5 22 L22.5 19.5 L27 21.5 L27 25.5 C27 26.5 26 27 25 27 C17 26.5 10 19.5 9.5 11.2 C9.5 10 10 9 11 9 Z" fill="var(--white)"/>
    </svg>
    <span>(555)210 - 0148</span>
  </div>

  <h1 class="title">Platelet Rich Plasma Therapy (PRP)</h1>

  <section class="info-box">
    <p class="info-line">Your own platelets, injected to speed healing.</p>
    <p class="info-line">Repairs damaged tendons and tissue.</p>
    <p class="info-line">Consultation required.</p>
    <p class="price">$199</p>
    <p class="price-note">FSA / HSA Eligible</p>
  </section>

  <p class="treating">Treating: Plantar Fasciitis<br>&nbsp;Achilles Tendonitis | Tendon &amp;<br>Ligament Injuries</p>

  <footer class="offices">
    <div class="office">
      <div class="office-name">Ashford Office</div>
      <div class="office-address">58 Larkspur Dr. Ste. 120<br>Ashford, MD 21890</div>
    </div>
    <div class="office">
      <div class="office-name">Cedar Falls Office</div>
      <div class="office-address">2210 Maplecrest Blvd. Ste. 304<br>Cedar Falls, MD 21893</div>
    </div>
    <div class="office">
      <div class="office-name">Millbrook Office</div>
      <div class="office-address">77 Willow Bend Lane<br>Millbrook, WV 25499</div>
    </div>
  </footer>
</main>
</body>
</html>
```